Construction site, small core-flute signage design required

Each building site requires a small sign (approx A4) that has my logo, company name, PO BOX address, website and phone number. I need a professional looking design. Please see attached my logos, and examples.

```html
<!DOCTYPE html>
<html lang="en">
<head>
<meta charset="utf-8">
<title>Principal Certifying Authority – Site Sign</title>
<link rel="stylesheet" href="https://fonts.googleapis.com/css2?family=Exo+2:wght@400;500;600&display=swap">
<style>
  :root{
    --page:#eef0f2;
    --card:#ffffff;
    --ink:#2f3d52;
    --label:#4c4f55;
    --rule:#5a5d63;
    --brand-blue:#0a6fb5;
    --brand-deep:#0b5a9a;
    --brand-mid:#0d63a6;
    --swoosh:#e6e7e9;
    --muted:#3d4046;
  }
  *{margin:0;padding:0;box-sizing:border-box}
  html,body{width:1200px;height:2610px;overflow:hidden;background:var(--page)}
  body{font-family:"Exo 2",sans-serif;position:relative}
  .sign{
    position:absolute;left:60px;top:922px;width:943px;height:670px;
    background:var(--card);overflow:hidden;
    transform:scale(1.1453);transform-origin:top left;
    box-shadow:0 4px 14px rgba(0,0,0,.18);
  }
  .sign__wave{position:absolute;inset:0;width:943px;height:670px}
  .sign__title{
    position:absolute;left:305px;top:46px;width:580px;text-align:center;
    font-size:33px;font-weight:500;color:var(--ink);letter-spacing:.2px;white-space:nowrap;
  }
  .brand{
    position:absolute;left:330px;top:160px;width:530px;
    display:flex;align-items:center;justify-content:center;gap:16px;
  }
  .brand__mark{width:34px;height:34px;background:var(--brand-blue);border-radius:4px}
  .brand__name{font-size:46px;font-weight:600;color:var(--ink);white-space:nowrap}
  .field{
    position:absolute;display:flex;align-items:flex-end;
    font-size:27px;font-weight:500;color:var(--label);white-space:nowrap;
  }
  .field__line{border-bottom:2px solid var(--rule);margin-left:8px;margin-bottom:7px;height:2px}
  .field--cc{left:258px;top:310px}
  .field--cc .field__line{width:470px}
  .field--builder{left:258px;top:400px}
  .field--builder .field__line{width:275px}
  .field--lic{left:656px;top:400px}
  .field--lic .field__line{width:138px}
  .field--phone{left:258px;top:490px}
  .field--phone .field__line{width:318px}
  .postal{position:absolute;left:347px;top:557px;color:var(--muted);font-style:normal}
  .postal__heading{font-size:20px;font-weight:600;color:var(--brand-blue);margin-bottom:6px}
  .postal__line{font-size:16px;line-height:20px;white-space:nowrap}
  .footer__divider{position:absolute;left:612px;top:565px;width:2px;height:68px;background:var(--ink)}
  .contact{
    position:absolute;left:630px;right:22px;display:flex;align-items:center;gap:10px;
    font-size:15px;color:var(--muted);white-space:nowrap;
  }
  .contact--web{top:572px}
  .contact--mail{top:602px}
  .contact strong{font-weight:600;color:var(--brand-deep)}
  .contact svg{width:19px;height:19px;flex:none}
</style>
</head>
<body>
  <main class="sign">
    <svg class="sign__wave" viewBox="0 0 943 670" aria-hidden="true">
      <path fill="var(--swoosh)" d="M0,0 H300 C250,90 170,210 158,380 C150,520 270,625 415,670 H0 Z"/>
      <path fill="var(--brand-deep)" d="M0,0 H262 C282,70 250,150 208,222 C158,322 146,470 190,560 C220,620 262,650 298,670 H0 Z"/>
      <path fill="var(--brand-blue)" d="M0,0 H248 C266,70 236,150 196,222 C148,322 136,470 180,560 C210,620 250,650 286,670 H0 Z"/>
      <path fill="var(--brand-mid)" d="M0,350 C60,290 120,260 170,235 C120,330 92,430 110,530 C122,600 160,645 200,670 H0 Z"/>
    </svg>

    <h1 class="sign__title">PRINCIPAL CERTIFYING AUTHORITY</h1>

    <div class="brand">
      <span class="brand__mark"></span>
      <span class="brand__name">Harbourline Certifiers</span>
    </div>

    <div class="field field--cc">CC/CDC No:<span class="field__line"></span></div>
    <div class="field field--builder">Builder:<span class="field__line"></span></div>
    <div class="field field--lic">Lic No:<span class="field__line"></span></div>
    <div class="field field--phone">Phone No:<span class="field__line"></span></div>

    <address class="postal">
      <p class="postal__heading">PO BOX address</p>
      <p class="postal__line">18 Marlow St, Coogee Ridge</p>
      <p class="postal__line">New South Wales, Australia, 2034</p>
    </address>

    <span class="footer__divider"></span>

    <p class="contact contact--web">
      <svg viewBox="0 0 20 20" aria-hidden="true">
        <circle cx="10" cy="10" r="9" fill="none" stroke="var(--ink)" stroke-width="1.2"/>
        <circle cx="10" cy="10" r="6" fill="none" stroke="var(--brand-blue)" stroke-width="1.2"/>
        <path d="M4,10 H16 M10,4 V16 M10,4 C7,7 7,13 10,16 M10,4 C13,7 13,13 10,16" fill="none" stroke="var(--brand-blue)" stroke-width="1"/>
      </svg>
      <span>www.<strong>harbourlinecertifiers</strong>.com.au</span>
    </p>
    <p class="contact contact--mail">
      <svg viewBox="0 0 20 20" aria-hidden="true">
        <circle cx="10" cy="10" r="9" fill="none" stroke="var(--ink)" stroke-width="1.2"/>
        <rect x="5.5" y="7" width="9" height="6.5" fill="var(--brand-blue)"/>
        <path d="M5.5,7 L10,11 L14.5,7" fill="none" stroke="#fff" stroke-width="1"/>
      </svg>
      <span>info@<strong>harbourlinecertifiers</strong>.com.au</span>
    </p>
  </main>
</body>
</html>
```